Consulting Company needs business card design

We need a business card design for a new consulting and business solutions company based in Bermuda called Corvale Partners Limited. Looking for a double sided business card with one side only including the company logo thats attached and the other including contact information. Logo contains blue and turquoise colors and is fine to be on both sides of the card.
Contact Information for Business Card
Corvale Partners Limited
P.O. Box HM318
Devonshire DV BX
Bermuda
Name: Marcus Pellegrin
Position: Director
Telephone: 1 441 733 4906
Email: mpellegrin@corvale.example
Website: www.corvale.example

```html
<!DOCTYPE html>
<html lang="en">
<head>
<meta charset="utf-8">
<title>Corvale Partners Limited — Business Card</title>
<link rel="stylesheet" href="https://fonts.googleapis.com/css2?family=Open+Sans:wght@400;600;700;800&display=swap">
<style>
  :root {
    --backdrop: #5b5b5b;
    --brand-blue: #27a9e1;
    --brand-teal: #12b3bd;
    --ink: #1c1c1c;
    --paper: #ffffff;
  }
  * { margin: 0; padding: 0; box-sizing: border-box; }
  html, body { width: 1200px; height: 1200px; overflow: hidden; }
  body {
    background: var(--backdrop);
    font-family: "Open Sans", sans-serif;
    position: relative;
  }
  .card {
    position: absolute;
    left: 150px;
    width: 900px;
    height: 514px;
    overflow: hidden;
  }
  .card--front { top: 58px; background: var(--brand-blue); }
  .card--back { top: 628px; background: var(--paper); }

  .wordmark {
    position: absolute;
    display: flex;
    align-items: center;
    gap: 18px;
  }
  .wordmark__dot { border-radius: 50%; flex: none; }
  .wordmark__name { font-weight: 700; letter-spacing: 1px; white-space: nowrap; }

  .card--front .wordmark { left: 50%; top: 50%; transform: translate(-50%, -50%); }
  .card--front .wordmark__dot { width: 70px; height: 70px; background: var(--paper); }
  .card--front .wordmark__name { color: var(--paper); font-size: 44px; }

  .card--back .wordmark { left: 70px; top: 150px; gap: 12px; }
  .card--back .wordmark__dot { width: 44px; height: 44px; background: var(--brand-blue); }
  .card--back .wordmark__name { color: var(--brand-blue); font-size: 24px; }

  .person { position: absolute; left: 470px; top: 88px; }
  .person__name { font-size: 40px; font-weight: 700; color: var(--ink); line-height: 1.1; }
  .person__role { font-size: 19px; color: var(--ink); letter-spacing: 0.5px; margin-top: 4px; }

  .divider {
    position: absolute;
    left: 150px; right: 70px; top: 262px;
    height: 3px; background: var(--brand-teal);
  }

  .address {
    position: absolute; left: 150px; top: 290px;
    list-style: none; font-size: 27px; line-height: 1.28; color: var(--ink);
  }

  .contacts {
    position: absolute; left: 520px; top: 292px;
    list-style: none; font-size: 23px; color: var(--ink);
  }
  .contacts li { display: flex; align-items: center; gap: 12px; height: 40px; }
  .contacts svg { width: 22px; height: 22px; flex: none; }

  .base-band {
    position: absolute; left: 0; right: 0; bottom: 0; height: 42px;
    background: linear-gradient(90deg, var(--brand-blue), var(--brand-teal));
  }
</style>
</head>
<body>
  <section class="card card--front" aria-label="Card front">
    <div class="wordmark">
      <span class="wordmark__dot"></span>
      <span class="wordmark__name">Corvale Partners Limited</span>
    </div>
  </section>

  <section class="card card--back" aria-label="Card back">
    <div class="wordmark">
      <span class="wordmark__dot"></span>
      <span class="wordmark__name">Corvale Partners Limited</span>
    </div>

    <div class="person">
      <p class="person__name">Marcus Pellegrin</p>
      <p class="person__role">DIRECTOR</p>
    </div>

    <div class="divider"></div>

    <ul class="address">
      <li>Corvale Partners Limited</li>
      <li>P.O. Box HM318</li>
      <li>Devonshire DV BX</li>
      <li>Bermuda</li>
    </ul>

    <ul class="contacts">
      <li>
        <svg viewBox="0 0 24 24" aria-hidden="true"><path fill="#12b3bd" d="M6.6 10.8a15.1 15.1 0 0 0 6.6 6.6l2.2-2.2a1 1 0 0 1 1-.25 11.4 11.4 0 0 0 3.6.57 1 1 0 0 1 1 1V20a1 1 0 0 1-1 1A17 17 0 0 1 3 4a1 1 0 0 1 1-1h3.5a1 1 0 0 1 1 1c0 1.25.2 2.45.57 3.57a1 1 0 0 1-.25 1z"/></svg>
        1 441 733 4906
      </li>
      <li>
        <svg viewBox="0 0 24 24" aria-hidden="true"><rect x="2" y="5" width="20" height="14" rx="1.5" fill="#12b3bd"/><path d="M2.5 6l9.5 7 9.5-7" fill="none" stroke="#fff" stroke-width="1.6"/></svg>
        mpellegrin@corvale.example
      </li>
      <li>
        <svg viewBox="0 0 24 24" aria-hidden="true"><g fill="none" stroke="#12b3bd" stroke-width="1.6"><circle cx="12" cy="12" r="9.5"/><ellipse cx="12" cy="12" rx="4.2" ry="9.5"/><path d="M2.5 12h19M4 7h16M4 17h16"/></g></svg>
        www.corvale.example
      </li>
    </ul>

    <div class="base-band"></div>
  </section>
</body>
</html>
```